business cards/stationary for construction company
FERN HOLLOW BUILDERS, LLC
Simple
GENERAL CONTRACTORS
PO Box 48315
Bozeman, MT 59284
fhbuilders.llc@postvale.net
We want two names and #'s on the cards:
Dana Whitcombe 702.555.0148 & Ryan Pettigrew 702.555.0193
new logo.. please take a look

```html
<!DOCTYPE html>
<html lang="en">
<head>
<meta charset="utf-8">
<title>Fern Hollow Builders – Stationery</title>
<link href="https://fonts.googleapis.com/css2?family=Cormorant+Garamond:wght@600&family=Open+Sans:wght@400;600&display=swap" rel="stylesheet">
<style>
:root{
  --bg:#e9e4dc;
  --paper:#ffffff;
  --ink:#3c4652;
  --muted:#8a929b;
  --slate:#5b6f86;
  --steel:#9aa8b8;
  --grey:#b9bcc0;
  --flap-blue:#7f95b0;
  --flap-grey:#8e9196;
  --shadow:0 2px 6px rgba(0,0,0,.25);
}
*{margin:0;padding:0;box-sizing:border-box}
html,body{width:1200px;height:446px;overflow:hidden}
body{background:var(--bg);position:relative;font-family:"Open Sans",sans-serif;color:var(--ink)}
.label{position:absolute;font-size:7px;color:#5a4a3a;letter-spacing:.03em}
.sheet{position:absolute;background:var(--paper);box-shadow:var(--shadow);overflow:hidden}
.brand{font-family:"Cormorant Garamond",serif;font-weight:600;color:var(--slate);white-space:nowrap}
.brand-mark{display:inline-block;width:.7em;height:.7em;border-radius:50%;background:var(--slate);margin-right:.3em;vertical-align:middle}
.swoosh{position:absolute;left:0;bottom:0;width:100%}
.contact{position:absolute;font-size:5px;color:var(--muted);line-height:1.9}
.contact svg{width:5px;height:5px;vertical-align:-1px;margin-right:3px}
.footer-line{position:absolute;left:0;right:0;bottom:12px;text-align:center;font-size:5px;color:var(--muted)}
.footer-line span{margin:0 6px}
.watermark{position:absolute;left:0;right:0;top:46%;text-align:center;font-size:24px;opacity:.12}
</style>
</head>
<body>

<div class="label" style="left:12px;top:72px">Stationery Concepts</div>

<!-- business card front -->
<div class="sheet card" style="left:14px;top:160px;width:122px;height:42px">
  <div class="brand" style="position:absolute;left:22px;top:13px;font-size:10px"><span class="brand-mark"></span>FernHollow Builders</div>
  <svg class="swoosh" viewBox="0 0 122 8" preserveAspectRatio="none" height="8"><path d="M0 5Q60 0 122 4V8H0Z" fill="var(--grey)"/><path d="M0 7Q60 3 122 6V8H0Z" fill="var(--slate)"/></svg>
</div>
<div class="label" style="left:14px;top:206px">Business Card Front</div>

<!-- business card back -->
<div class="sheet card" style="left:14px;top:236px;width:122px;height:46px">
  <div class="brand" style="position:absolute;left:6px;top:6px;font-size:7px"><span class="brand-mark"></span>FernHollow Builders</div>
  <div class="contact" style="left:8px;top:18px;line-height:1.5;font-size:4.5px">Dana Whitcombe 702.555.0148<br>Ryan Pettigrew 702.555.0193</div>
  <svg class="swoosh" viewBox="0 0 122 8" preserveAspectRatio="none" height="8"><path d="M0 5Q60 0 122 4V8H0Z" fill="var(--grey)"/><path d="M0 7Q60 3 122 6V8H0Z" fill="var(--slate)"/></svg>
</div>
<div class="label" style="left:14px;top:286px">Business Card Back</div>

<!-- letterhead option 1 -->
<div class="sheet letterhead" style="left:163px;top:19px;width:308px;height:400px">
  <div class="brand" style="position:absolute;left:24px;top:40px;font-size:12px"><span class="brand-mark"></span>FernHollow Builders, LLC</div>
  <div class="contact" style="left:212px;top:20px">
    <div><svg viewBox="0 0 10 10"><circle cx="5" cy="5" r="4" fill="var(--muted)"/></svg>702.555.0148</div>
    <div><svg viewBox="0 0 10 10"><path d="M5 0a3.5 3.5 0 0 1 3.5 3.5C8.5 6 5 10 5 10S1.5 6 1.5 3.5A3.5 3.5 0 0 1 5 0Z" fill="var(--muted)"/></svg>PO Box 48315, Bozeman, MT 59284</div>
    <div><svg viewBox="0 0 10 10"><rect x="0" y="2" width="10" height="6" fill="var(--muted)"/></svg>fhbuilders.llc@postvale.net</div>
  </div>
  <svg class="swoosh" viewBox="0 0 308 40" preserveAspectRatio="none" height="40"><path d="M0 18Q150 0 308 14V40H0Z" fill="var(--grey)"/><path d="M0 28Q160 10 308 24V40H0Z" fill="var(--steel)"/><path d="M0 36Q160 22 308 32V40H0Z" fill="var(--slate)"/></svg>
</div>
<div class="label" style="left:290px;top:424px">Letterhead Option 1</div>

<!-- letterhead option 2 -->
<div class="sheet letterhead" style="left:492px;top:19px;width:308px;height:400px">
  <div class="brand watermark">FernHollow Builders</div>
  <div class="footer-line"><span>PO Box 48315, Bozeman, MT 59284</span><span>fhbuilders.llc@postvale.net</span><span>702.555.0148</span></div>
  <svg class="swoosh" viewBox="0 0 308 10" preserveAspectRatio="none" height="10"><path d="M0 6Q150 0 308 5V10H0Z" fill="var(--grey)"/><path d="M0 9Q150 4 308 8V10H0Z" fill="var(--slate)"/></svg>
</div>
<div class="label" style="left:620px;top:424px">Letterhead Option 2</div>

<!-- envelope backs -->
<svg class="sheet envelope" style="left:828px;top:19px;box-shadow:var(--shadow)" width="353" height="125" viewBox="0 0 353 125"><rect width="353" height="125" fill="#e6ebf1"/><path d="M0 0H353L176 70Z" fill="var(--flap-blue)"/></svg>
<svg class="sheet envelope" style="left:828px;top:92px;box-shadow:var(--shadow)" width="353" height="135" viewBox="0 0 353 135"><rect width="353" height="135" fill="#f1f1f1"/><path d="M0 0H353L176 70Z" fill="var(--flap-grey)"/></svg>

<!-- envelope front -->
<div class="sheet envelope" style="left:828px;top:158px;width:353px;height:105px">
  <div class="brand" style="position:absolute;left:138px;top:46px;font-size:12px"><span class="brand-mark"></span>FernHollow Builders, LLC</div>
</div>

<!-- envelope front with return address -->
<div class="sheet envelope" style="left:828px;top:265px;width:353px;height:155px">
  <div class="brand" style="position:absolute;left:14px;top:18px;font-size:11px"><span class="brand-mark"></span>FernHollow Builders, LLC</div>
  <div class="contact" style="left:16px;top:36px;line-height:1.6">PO Box 48315, Bozeman, MT 59284</div>
  <svg class="swoosh" viewBox="0 0 353 24" preserveAspectRatio="none" height="24"><path d="M0 12Q170 0 353 10V24H0Z" fill="var(--grey)"/><path d="M0 20Q170 8 353 18V24H0Z" fill="var(--slate)"/></svg>
</div>
<div class="label" style="left:970px;top:424px">Envelope Option 1</div>

</body>
</html>
```